Webbanner-Design für Informatik Dienstleistungen und Webdesign
Zielgruppe
Informatik Dienstleistungen und Webdesign
Aufgabenstellung
Es soll immer das gleiche Gesicht auf den Banner und ein kurzer Satz.
1. Sie haben das Business - wir die Software
2. Sie haben Anforderungen - wir Lösungen
3. Sie brauchen Unterstützung - wir helfen
Die Banner sollen auf unserer Homepage www.vendrak-media.ch auf der Startseite durchlaufen. Das Format soll 1200x500 Pixel sein

```html
<!DOCTYPE html>
<html lang="de">
<head>
<meta charset="utf-8">
<title>Sie haben Anforderungen – wir Lösungen</title>
<link rel="stylesheet" href="https://fonts.googleapis.com/css2?family=Arimo:ital,wght@1,400;1,700&display=swap">
<style>
  :root {
    --panel-dark: #1b1b1b;
    --panel-dark-soft: #2b2b2b;
    --canvas-white: #ffffff;
    --ink-black: #111111;
    --headline-white: #ffffff;
    --portrait-top: #c9b294;
    --portrait-bottom: #151515;
  }
  html, body {
    margin: 0;
    padding: 0;
    overflow: hidden;
    background: var(--canvas-white);
  }
  .banner {
    position: relative;
    width: 1200px;
    height: 500px;
    overflow: hidden;
    background: var(--canvas-white);
    font-family: "Arimo", Arial, sans-serif;
  }
  .banner__backdrop {
    position: absolute;
    inset: 0;
  }
  .headline {
    position: absolute;
    left: 22px;
    top: 186px;
    margin: 0;
    color: var(--headline-white);
    font-style: italic;
    font-weight: 400;
    font-size: 44px;
    line-height: 1;
    letter-spacing: 0.2px;
  }
  .headline__strong {
    font-weight: 700;
  }
  .answer {
    position: absolute;
    left: 22px;
    top: 246px;
    display: flex;
    align-items: flex-end;
  }
  .answer__box {
    display: inline-block;
    background: var(--canvas-white);
    color: var(--ink-black);
    font-style: italic;
    font-weight: 700;
    font-size: 44px;
    line-height: 62px;
    height: 62px;
    padding: 0 24px 0 18px;
  }
  .answer__dot {
    color: var(--headline-white);
    font-style: italic;
    font-weight: 700;
    font-size: 44px;
    line-height: 1;
    margin-left: 14px;
    margin-bottom: 2px;
  }
</style>
</head>
<body>
  <div class="banner">
    <svg class="banner__backdrop" width="1200" height="500" viewBox="0 0 1200 500" xmlns="http://www.w3.org/2000/svg">
      <defs>
        <linearGradient id="darkPanelTone" x1="0" y1="0" x2="1" y2="1">
          <stop offset="0" stop-color="var(--panel-dark-soft)"/>
          <stop offset="1" stop-color="var(--panel-dark)"/>
        </linearGradient>
        <linearGradient id="portraitTone" x1="0" y1="0" x2="0" y2="1">
          <stop offset="0" stop-color="var(--portrait-top)"/>
          <stop offset="0.4" stop-color="var(--portrait-bottom)"/>
          <stop offset="1" stop-color="var(--portrait-bottom)"/>
        </linearGradient>
      </defs>
      <polygon points="0,0 815,0 555,500 0,500" fill="url(#darkPanelTone)"
               role="img" aria-label="Dunkles Foto: Hand zeigt auf Wireframe-Skizzen an einer Wand"/>
      <rect x="795" y="18" width="325" height="482" rx="60" fill="url(#portraitTone)"
            role="img" aria-label="Porträt einer lächelnden Frau mit langen blonden Haaren im schwarzen Sportshirt, Arme verschränkt"/>
    </svg>

    <p class="headline">Sie haben <span class="headline__strong">Anforderungen</span></p>
    <div class="answer">
      <span class="answer__box">wir Lösungen</span>
      <span class="answer__dot">.</span>
    </div>
  </div>
</body>
</html>
```